Flyer for New Spa Opening

We need a flyer to increase customer's awareness of our new spa located in Yangon, Myanmar, in a middle-upper class shopping mall. A new hotel will be opening above the mall in Dec 2013.
Updates

Have made payment guaranteed.  Need a good flyer. Thanks.

Hi, I have uploaded a Words File for Flyer Text. Thanks!

Dear Designers,

I have setup a 2nd award, there's too many outstanding designs! Thanks so much.

Regards
Marla

Target Market(s)

-Hotel guest who wants to a spa session to relax
-Woman between 18 - 55 years old who have high spending power in a poor country(Myanmar). They like to use "Big Brands" but do not have much variety available in their country.

Industry/Entity Type

Shopping

Requirements
Must have
• Our services include Body Spa, Facial, Nails, Waxing & Foot Reflexology. We use well-known international brands in our spa including Veridelle, KRU, Varnet, Brisola Terrano and MORLU.

Veridelle, the skin care system researched and developed by The Halvern Dermal Academy (HDA), is an international leader in today’s skin care industry.

We are authorized Veridelle skin spa to provide professional facial and retailing Veridelle products.

Include the logo of the brands

Willowmere Spa
add: No 72, Thuka Road, Min Ye Plaza (Level-5) (6187), Kyimyin Township, Yangon
tel: +959 47208613
email: contactus@velmora-unitedgroup.example

Nice to have
• visually nice and relaxing spa pictures.
Should not have
• price

```html
<!DOCTYPE html>
<html lang="en">
<head>
<meta charset="utf-8">
<title>Willowmere Spa Flyer</title>
<link rel="stylesheet" href="https://fonts.googleapis.com/css2?family=Arimo:wght@400;700&family=Oswald:wght@700&display=swap">
<style>
  :root {
    --canvas-grey: #c9c9c9;
    --paper: #ffffff;
    --spa-red: #d8261d;
    --title-red: #b3201c;
    --heading-maroon: #8e1010;
    --service-red: #cc1f1f;
    --pink-soft: #f4c9d5;
    --mauve: #b9536e;
    --body-text: #2b2b2b;
    --brand-text: #222222;
    --hairline: #9a9a9a;
    --white: #ffffff;
  }
  * { margin: 0; padding: 0; box-sizing: border-box; }
  html, body { width: 1200px; height: 950px; overflow: hidden; }
  body { background: var(--canvas-grey); position: relative; font-family: "Arimo", Arial, sans-serif; }

  .flyer {
    position: absolute; left: 26px; top: 26px;
    width: 1148px; height: 898px;
    background: var(--paper); overflow: hidden;
  }
  .flyer__art { position: absolute; left: 0; top: 0; width: 1148px; height: 898px; }

  .about { position: absolute; left: 52px; top: 50px; width: 310px; }
  .about__title {
    font-family: "Oswald", sans-serif; font-weight: 700;
    font-size: 25px; color: var(--heading-maroon); letter-spacing: -0.3px;
    margin-bottom: 12px;
  }
  .about__text { font-size: 13.6px; line-height: 19.8px; color: var(--body-text); }

  .brands {
    position: absolute; left: 104px; top: 382px; width: 220px;
    font-family: "Arimo", sans-serif; font-weight: 700; font-size: 15px;
    line-height: 22px; color: var(--brand-text);
  }
  .brands__name { display: inline-block; margin-right: 12px; }

  .services { position: absolute; left: 410px; top: 62px; }
  .services__title { font-size: 16.5px; font-weight: 700; color: var(--service-red); letter-spacing: 0.2px; margin-bottom: 22px; margin-left: 10px; }
  .services__list { list-style: none; }
  .services__item {
    font-size: 10.5px; font-weight: 700; color: var(--service-red);
    height: 25px; display: flex; align-items: center;
  }
  .services__item::before {
    content: ""; width: 10px; height: 10px; border-radius: 50%;
    background: var(--white); box-shadow: 0 0 2px rgba(0,0,0,0.35);
    margin-right: 7px;
  }

  .brand-title {
    position: absolute; left: 660px; top: 222px; width: 440px;
    text-align: center;
    font-family: "Arimo", sans-serif; font-weight: 700;
    font-size: 56px; line-height: 66px; color: var(--title-red);
  }

  .contact {
    position: absolute; left: 406px; top: 778px;
    font-size: 13px; font-weight: 700; line-height: 19px; color: var(--white);
    font-style: normal;
  }
</style>
</head>
<body>
<main class="flyer">
  <svg class="flyer__art" viewBox="0 0 956 748" preserveAspectRatio="none">
    <defs>
      <linearGradient id="paperShade" x1="0" y1="0" x2="0.3" y2="1">
        <stop offset="0" stop-color="#ffffff"/>
        <stop offset="1" stop-color="#e6e6e6"/>
      </linearGradient>
      <linearGradient id="photoTones" x1="0.2" y1="0" x2="0.5" y2="1">
        <stop offset="0" stop-color="#fbe9ee"/>
        <stop offset="0.35" stop-color="#f2b6c2"/>
        <stop offset="0.6" stop-color="#e24b48"/>
        <stop offset="0.85" stop-color="#e9c3b4"/>
        <stop offset="1" stop-color="#d93a33"/>
      </linearGradient>
    </defs>

    <rect class="paper-bg" width="956" height="748" fill="url(#paperShade)"/>

    <path class="photo-area" role="img" aria-label="Photo of hands with glossy red manicured nails resting on rose petals"
      d="M0,518 C250,470 380,380 500,240 C600,120 700,45 956,60 L956,748 L0,748 Z"
      fill="url(#photoTones)"/>

    <path class="swoosh-line" d="M300,330 C450,250 540,120 690,85 C800,60 900,85 956,95" fill="none" stroke="var(--hairline)" stroke-width="0.9"/>
    <path class="swoosh-line" d="M0,560 C200,500 380,470 600,500 C760,522 880,500 956,470" fill="none" stroke="#f5d6dc" stroke-width="0.9"/>

    <path class="swoosh-band" fill="var(--spa-red)"
      d="M0,430 C230,420 360,330 470,205 C580,80 700,10 956,22 L956,60 C700,45 600,120 500,240 C380,380 250,470 0,518 Z"/>

    <path class="wave-stripe" fill="var(--pink-soft)"
      d="M0,648 C150,578 300,540 430,563 C580,590 780,600 956,500 L956,532 C780,630 580,620 430,592 C300,568 150,606 0,680 Z"/>
    <path class="wave-line" fill="none" stroke="var(--mauve)" stroke-width="3"
      d="M0,672 C150,598 300,560 430,584 C580,612 780,622 956,524"/>
    <path class="wave-base" fill="var(--spa-red)"
      d="M0,690 C150,620 300,582 430,604 C580,630 780,636 956,538 L956,748 L0,748 Z"/>
    <path class="wave-glow" fill="#e85a55" opacity="0.55"
      d="M0,710 C120,660 220,640 320,640 C220,660 120,700 0,738 Z"/>
  </svg>

  <section class="about">
    <h2 class="about__title">About us:</h2>
    <p class="about__text">Veridelle, the skin care system researched and developed by The Halvern Dermal Academy (HDA), is an international leader in today’s skin care industry.<br>We are authorized Veridelle skin spa to provide professional facial and retailing Veridelle products.<br>We use well-known international brands in our spa including Veridelle, KRU, Varnet, Brisola Terrano and MORLU.</p>
  </section>

  <div class="brands" aria-label="Partner brands">
    <span class="brands__name">Veridelle</span>
    <span class="brands__name">KRU</span>
    <span class="brands__name">MORLU</span>
  </div>

  <section class="services">
    <h2 class="services__title">OUR SERVICES INCLUDE:</h2>
    <ul class="services__list">
      <li class="services__item">BODY SPA</li>
      <li class="services__item">FACIAL</li>
      <li class="services__item">NAILS</li>
      <li class="services__item">WAXING</li>
      <li class="services__item">FOOT REFLEXOLOGY</li>
    </ul>
  </section>

  <h1 class="brand-title">Willowmere<br>Spa</h1>

  <address class="contact">
    Address:&nbsp; No 72, Thuka Road, Min Ye Plaza<br>
    (Level-5) (6187), Kyimyin Township, Yangon<br>
    tel.: +959 47208613<br>
    email: contactus@velmora-unitedgroup.example
  </address>
</main>
</body>
</html>
```